Awesome ecommerce store banner needed!

We need a sharp, clear, strong banner for one of our subcategory pages on http://www.brivelloop.example
We'd like to incorporate the following image. We'd like the background to be gray or black. We are replacing the Wireless Intercoms banner that is orange (we hate it).
WE do like our other banners, however, so please use them as reference:
SIze: 980 x 380
Two raw images of the intercom we'd like you to encorporate have been included. Choose one or the other depending on what you think would be best. If using the single angle, please duplicate it. We want two intercoms in the banner
Simple and Clean is key:
Text: Wireless Intercoms
Text Color: Can be white/off gray
Text Style: Please keep it clean in line with the website
Background: Black/gray/white

```html
<!DOCTYPE html>
<html lang="en">
<head>
<meta charset="utf-8">
<title>Wireless Intercoms – Brivelloop</title>
<link rel="stylesheet" href="https://fonts.googleapis.com/css2?family=Saira+Condensed:wght@800&family=Bebas+Neue&family=Oswald:wght@700&display=swap">
<style>
  :root {
    --bg-light: #eef0f2;
    --bg-mid: #c3c8cd;
    --band-dark: #1b1d1f;
    --band-mid: #34383b;
    --band-light: #6c7175;
    --title-hi: #ffffff;
    --title-lo: #8e959b;
    --ink: #1a1a1a;
    --cta-top: #e0301e;
    --cta-bottom: #8e0c05;
    --cta-text: #ffffff;
    --device-dark: #1c1f22;
    --device-mid: #5b6066;
    --device-light: #c9ced3;
  }
  html, body {
    margin: 0;
    padding: 0;
    overflow: hidden;
  }
  .banner {
    position: relative;
    width: 1200px;
    height: 465px;
    overflow: hidden;
    background: radial-gradient(ellipse at 35% 100%, var(--bg-light) 0%, var(--bg-mid) 85%);
  }
  .banner__band {
    position: absolute;
    left: 0;
    top: 58px;
    width: 1200px;
    height: 254px;
    background: linear-gradient(100deg, var(--band-dark) 0%, var(--band-mid) 45%, var(--band-light) 75%, rgba(150,155,160,0.5) 100%);
  }
  .banner__product {
    position: absolute;
    left: 620px;
    top: 0;
    width: 562px;
    height: 361px;
    border-radius: 0 0 60px 60px;
    background:
      linear-gradient(125deg, var(--device-dark) 0%, var(--device-dark) 35%, var(--device-mid) 55%, var(--device-light) 80%, #aeb4ba 100%);
    opacity: 0.92;
  }
  .banner__title {
    position: absolute;
    left: 76px;
    top: 48px;
    margin: 0;
    font-family: "Saira Condensed", "Arial Narrow", sans-serif;
    font-weight: 800;
    font-size: 118px;
    line-height: 128px;
    letter-spacing: 0;
    text-transform: uppercase;
    transform: skewX(-12deg);
    transform-origin: left bottom;
    background: linear-gradient(180deg, var(--title-hi) 0%, #e4e7ea 45%, var(--title-lo) 100%);
    -webkit-background-clip: text;
    background-clip: text;
    color: transparent;
    filter: drop-shadow(3px 4px 4px rgba(0,0,0,0.6));
  }
  .banner__title span { display: block; }
  .banner__tagline {
    position: absolute;
    left: 64px;
    top: 369px;
    margin: 0;
    font-family: "Bebas Neue", "Arial Narrow", sans-serif;
    font-size: 25px;
    line-height: 33px;
    letter-spacing: 1px;
    color: var(--ink);
  }
  .banner__cta {
    position: absolute;
    left: 478px;
    top: 371px;
    width: 244px;
    height: 64px;
    border-radius: 6px;
    background: linear-gradient(180deg, var(--cta-top) 0%, var(--cta-bottom) 100%);
    box-shadow: 0 2px 5px rgba(0,0,0,0.35);
    display: flex;
    align-items: center;
    justify-content: center;
    font-family: "Oswald", "Arial Narrow", sans-serif;
    font-weight: 700;
    font-size: 30px;
    color: var(--cta-text);
    text-decoration: none;
    letter-spacing: 0.5px;
  }
</style>
</head>
<body>
  <div class="banner">
    <div class="banner__band"></div>

    <div class="banner__product" role="img" aria-label="Product photo: two wireless intercom units with antennas, black control panels and silver speaker grilles"></div>

    <h1 class="banner__title"><span>Wireless</span><span>Intercoms</span></h1>

    <p class="banner__tagline">Browse products that makes wireless<br>home communication easy !</p>

    <a class="banner__cta" href="http://www.brivelloop.example">SHOP NOW &gt;</a>
  </div>
</body>
</html>
```